Fireworks company

COLORFUL design, incorporating logo (attached).
Information to be included:
PO BOX 4829
Marlow Vale 3891
Ph 03 5461 8237
Fax 03 5387 9216
Email sales@brindarockets.com.au
Web www.brindarockets.com.au

Check out our website for more inspiration? :-)

```html
<!DOCTYPE html>
<html lang="en">
<head>
<meta charset="utf-8">
<title>Brinda Rockets Letterhead</title>
<link rel="stylesheet" href="https://fonts.googleapis.com/css2?family=Bitter:wght@400;700&display=swap">
<style>
  :root {
    --backdrop: #e9e6e2;
    --paper: #ffffff;
    --brand-orange: #ff4a0a;
    --swoosh-brown: #5a2a0c;
    --ink: #1e1e1e;
    --icon-red: #e8202a;
    --house-brown: #6b2b10;
    --glow: #fbe7b8;
  }
  * { margin: 0; padding: 0; box-sizing: border-box; }
  html, body { width: 933px; height: 1200px; overflow: hidden; background: var(--backdrop); }
  body { position: relative; font-family: "Bitter", Georgia, serif; color: var(--ink); }

  .letterhead {
    position: absolute; left: 59px; top: 92px; width: 828px; height: 1071px;
    background: var(--paper); overflow: hidden;
  }
  .backdrop-glow {
    position: absolute; left: 400px; top: 0; width: 428px; height: 460px;
    background: radial-gradient(circle at 62% 55%, var(--glow) 0%, rgba(251,231,184,0.55) 30%, rgba(255,255,255,0) 65%);
  }
  .brand-name {
    position: absolute; font-weight: 700; line-height: 1;
    letter-spacing: 1px; text-transform: uppercase;
  }
  .brand-name--top { left: 32px; top: 34px; font-size: 30px; color: var(--brand-orange); }
  .brand-name--bottom { left: 636px; top: 993px; font-size: 21px; color: #fff; }
  .brand-name span { display: block; }
  .brand-name .line-two { font-size: 1.25em; margin-top: 4px; }

  .address {
    position: absolute; left: 607px; top: 50px; padding-left: 16px;
    border-left: 1.5px solid var(--ink); font-size: 15px; line-height: 20px;
  }
  .address svg { position: absolute; left: 16px; top: 3px; }
  .address p { padding-left: 26px; }

  .swoosh { position: absolute; left: 0; top: 0; }

  .contact-list {
    position: absolute; left: 10px; top: 947px; list-style: none; font-size: 15px;
  }
  .contact-list li { display: flex; align-items: center; height: 25px; }
  .contact-list svg { width: 22px; margin-right: 8px; flex: none; }
</style>
</head>
<body>
  <main class="letterhead">
    <div class="backdrop-glow" role="img" aria-label="Faint fireworks burst decoration"></div>

    <div class="brand-name brand-name--top"><span>Brinda</span><span class="line-two">Rockets</span></div>

    <div class="address">
      <svg width="18" height="16" viewBox="0 0 18 16" aria-hidden="true"><path d="M9 0 0 8h2.5v8h4.5v-5h4v5h4.5V8H18z" fill="var(--house-brown)"/></svg>
      <p>PO BOX 4829</p>
      <p>Marlow Vale 3891</p>
    </div>

    <svg class="swoosh" width="828" height="1071" viewBox="0 0 828 1071" aria-hidden="true">
      <path d="M828 780 C800 930 450 1055 0 1068 C470 1058 790 955 828 830 Z" fill="var(--swoosh-brown)"/>
      <path d="M828 842 C790 975 480 1060 40 1071 L828 1071 Z" fill="var(--brand-orange)"/>
    </svg>

    <div class="brand-name brand-name--bottom"><span>Brinda</span><span class="line-two">Rockets</span></div>

    <ul class="contact-list">
      <li><svg viewBox="0 0 22 16" aria-hidden="true"><rect x="3" y="0" width="10" height="6" fill="var(--icon-red)"/><rect x="1" y="6" width="18" height="9" rx="2" fill="var(--icon-red)"/></svg>03 5387 9216</li>
      <li><svg viewBox="0 0 22 18" aria-hidden="true"><circle cx="9" cy="9" r="8" fill="none" stroke="var(--icon-red)" stroke-width="1.5"/><path d="M6 4c-1 3 1 8 5 10l1.5-2-2-1.5-1 1c-1-1-2-3-2-4l1-1-1-2.5z" fill="var(--icon-red)"/></svg>03 5461 8237</li>
      <li><svg viewBox="0 0 22 14" aria-hidden="true"><rect x="0" y="1" width="20" height="12" fill="var(--icon-red)"/><path d="M0 1l10 7 10-7" fill="none" stroke="#fff" stroke-width="1.5"/></svg>sales@brindarockets.com.au</li>
      <li><svg viewBox="0 0 22 18" aria-hidden="true"><g fill="none" stroke="var(--icon-red)" stroke-width="1.4"><circle cx="9" cy="9" r="8"/><ellipse cx="9" cy="9" rx="3.5" ry="8"/><path d="M1 9h16M2.5 5h13M2.5 13h13"/></g></svg>www.brindarockets.com.au</li>
    </ul>
  </main>
</body>
</html>
```